Logo and business card for optometric practice
Curtis Hallorann & Associates
Marta Pelovska, O.D.
Oscar Tremwitz, O.D.
Neil Borromi, O.D.
417 Pembrook Parkway
Rockville Centre, New York 11570
516-902-4471

Target Market(s)

Patients, general public

Industry/Entity Type

Business

Logo Text

Curtis Hallorann & Associates Optometrists

Logo styles of interest
Pictorial/Combination Logo
Font styles to use
Serif
Sans Serif

Requirements
Must have
• current inspiration: realistic or photo closeup of eye, with interesting treatment of the iris OR
tech look, with closeup of eye and grid like the doctor is looking through a camera or microscope to view the eye up close
Should not have
• NO cartoons

```html
<!DOCTYPE html>
<html lang="en">
<head>
<meta charset="utf-8">
<title>Curtis Hallorann &amp; Associates — Stationery</title>
<link href="https://fonts.googleapis.com/css2?family=Jost:wght@400;500;600&display=swap" rel="stylesheet">
<style>
  :root {
    --ink: #0c0c0e;
    --blue: #2f5aa8;
    --blue-light: #4d93d8;
    --navy: #263a80;
    --brand: #34508e;
    --paper: #ffffff;
    --stage: #eeeeef;
    --grey-text: #d4d4d8;
    --faint: #d7e1ef;
  }
  * { box-sizing: border-box; margin: 0; padding: 0; }
  html, body { width: 1200px; height: 1000px; overflow: hidden; }
  body {
    background: var(--stage);
    font-family: "Jost", "Futura", sans-serif;
    position: relative;
  }
  .piece { position: absolute; overflow: hidden; box-shadow: 0 4px 14px rgba(0,0,0,.22); }
  .piece > svg.shape { position: absolute; inset: 0; width: 100%; height: 100%; }

  .brand { position: absolute; font-weight: 400; text-transform: uppercase; line-height: 1; }
  .brand .name { display: block; letter-spacing: .01em; }
  .brand .sub { display: block; letter-spacing: .42em; margin-top: .25em; }
  .brand-dot { position: absolute; border-radius: 50%; background: var(--blue); }

  .logo-master { position: absolute; left: 50px; top: 80px; width: 430px; height: 210px; }
  .logo-master .brand-dot { left: 183px; top: 20px; width: 64px; height: 64px; }
  .logo-master .brand { left: 0; top: 125px; width: 430px; text-align: center; color: var(--brand); }
  .logo-master .name { font-size: 44px; }
  .logo-master .sub { font-size: 17px; }

  .chips { position: absolute; display: flex; gap: 8px; }
  .chip {
    background: var(--navy); color: #fff; font-weight: 600;
    border: 2px solid #fff; outline: 1.5px solid var(--ink);
    padding: 2px 8px; font-size: 9px; letter-spacing: .02em; white-space: nowrap;
  }
  .address { position: absolute; color: #fff; font-size: 8.5px; letter-spacing: .02em; white-space: nowrap; }

  /* letterhead */
  .letterhead { left: 490px; top: 60px; width: 665px; height: 905px; background: var(--paper); }
  .letterhead .brand { left: 28px; top: 50px; color: #fff; }
  .letterhead .name { font-size: 16px; }
  .letterhead .sub { font-size: 7px; }
  .letterhead .brand-dot { left: 70px; top: 16px; width: 26px; height: 26px; }
  .letterhead .footer { position: absolute; left: 0; right: 0; bottom: 0; height: 82px; background: var(--ink); }
  .letterhead .chips { left: 235px; top: -14px; gap: 12px; }
  .letterhead .chip { font-size: 10px; padding: 4px 10px; }
  .letterhead .address { left: 235px; width: 400px; top: 36px; text-align: center; font-size: 9px; }

  /* window envelope */
  .envelope-window { left: 40px; top: 272px; width: 665px; height: 300px; background: var(--paper); }
  .envelope-window .brand.header { left: 40px; top: 100px; color: #fff; }
  .envelope-window .header .name { font-size: 14px; }
  .envelope-window .header .sub { font-size: 6px; }
  .envelope-window .brand-dot { left: 80px; top: 78px; width: 20px; height: 20px; }
  .envelope-window .brand.watermark { right: 50px; top: 172px; color: var(--faint); }
  .envelope-window .watermark .name { font-size: 30px; }
  .envelope-window .watermark .sub { font-size: 12px; }
  .envelope-window .window { position: absolute; left: 60px; top: 205px; width: 240px; height: 80px; background: #f1f1f2; border: 1px solid #bdbdc2; }
  .envelope-window .chips { right: 40px; top: 238px; }
  .envelope-window .address { right: 58px; top: 266px; }

  /* address envelope */
  .envelope-address { left: 40px; top: 590px; width: 665px; height: 345px; background: var(--ink); }
  .envelope-address .brand.title { left: 230px; top: 72px; color: #fff; }
  .envelope-address .title .name { font-size: 26px; }
  .envelope-address .title .sub { font-size: 11px; }
  .envelope-address .brand.side { left: 32px; top: 180px; color: #fff; }
  .envelope-address .side .name { font-size: 13px; }
  .envelope-address .side .sub { font-size: 6px; }
  .envelope-address .brand-dot { left: 72px; top: 150px; width: 22px; height: 22px; }
  .envelope-address .window { position: absolute; left: 190px; top: 120px; width: 445px; height: 170px; background: var(--paper); }
  .envelope-address .chips { left: 300px; top: 298px; }
  .envelope-address .address { left: 300px; width: 330px; text-align: center; top: 324px; }

  /* business card front */
  .card-front { left: 745px; top: 240px; width: 335px; height: 198px; background: var(--ink); }
  .card-front .brand { left: 0; top: 96px; width: 335px; text-align: center; color: #fff; }
  .card-front .name { font-size: 22px; }
  .card-front .sub { font-size: 9px; }
  .card-front .brand-dot { left: 146px; top: 40px; width: 42px; height: 42px; }

  /* business card back */
  .card-back { left: 868px; top: 415px; width: 322px; height: 180px; background: var(--ink); }
  .card-back .brand { left: 20px; top: 80px; color: #fff; }
  .card-back .name { font-size: 13px; }
  .card-back .sub { font-size: 6px; }
  .card-back .brand-dot { left: 68px; top: 46px; width: 26px; height: 26px; }
  .card-back .divider { position: absolute; left: 154px; top: 12px; width: 1.5px; height: 150px; background: #e8e8ea; }
  .card-back .details { position: absolute; left: 172px; top: 30px; color: var(--grey-text); font-size: 8.5px; line-height: 1.3; }
  .card-back .doctor { color: var(--blue-light); font-size: 12px; font-weight: 500; margin-bottom: 14px; }
  .card-back .block { margin-bottom: 12px; }
</style>
</head>
<body>

  <section class="logo-master">
    <span class="brand-dot"></span>
    <div class="brand"><span class="name">Curtis Hallorann</span><span class="sub">&amp; Associates</span></div>
  </section>

  <section class="piece letterhead">
    <svg class="shape" viewBox="0 0 665 905" preserveAspectRatio="none" aria-hidden="true">
      <defs>
        <linearGradient id="lh-band" x1="0" x2="1"><stop offset="0" stop-color="#2a4e9c"/><stop offset=".5" stop-color="#4d93d8"/><stop offset="1" stop-color="#2f4f9e"/></linearGradient>
      </defs>
      <path d="M0 0 H665 V40 Q330 92 0 80 Z" fill="#0c0c0e"/>
      <path d="M0 80 Q330 92 665 40 V48 Q330 120 0 106 Z" fill="url(#lh-band)"/>
      <path d="M0 80 Q330 92 665 40" fill="none" stroke="#fff" stroke-width="2"/>
    </svg>
    <span class="brand-dot"></span>
    <div class="brand"><span class="name">Curtis Hallorann</span><span class="sub">&amp; Associates</span></div>
    <footer class="footer">
      <div class="chips"><span class="chip">T 728 902 4471</span><span class="chip">F 728 902 4478</span><span class="chip">office@hallorann-eye.com</span></div>
      <p class="address">417 Pembrook Parkway Cedarbrook Falls, NY 11893</p>
    </footer>
  </section>

  <section class="piece envelope-window">
    <svg class="shape" viewBox="0 0 665 300" preserveAspectRatio="none" aria-hidden="true">
      <defs>
        <linearGradient id="ew-band" x1="0" x2="1"><stop offset="0" stop-color="#2a4e9c"/><stop offset=".5" stop-color="#4d93d8"/><stop offset="1" stop-color="#2f4f9e"/></linearGradient>
      </defs>
      <path d="M0 0 H665 V40 Q360 130 0 155 Z" fill="#0c0c0e"/>
      <path d="M0 155 Q360 130 665 40 V76 Q360 155 0 172 Z" fill="url(#ew-band)"/>
      <path d="M0 155 Q360 130 665 40" fill="none" stroke="#fff" stroke-width="2"/>
      <path d="M0 290 L665 222 V300 H0 Z" fill="#0c0c0e"/>
    </svg>
    <span class="brand-dot"></span>
    <div class="brand header"><span class="name">Curtis Hallorann</span><span class="sub">&amp; Associates</span></div>
    <div class="brand watermark"><span class="name">Curtis Hallorann</span><span class="sub">&amp; Associates</span></div>
    <div class="window"></div>
    <div class="chips"><span class="chip">T 728 902 4471</span><span class="chip">F 728 902 4478</span><span class="chip">office@hallorann-eye.com</span></div>
    <p class="address">417 Pembrook Parkway Cedarbrook Falls, NY 11893</p>
  </section>

  <section class="piece envelope-address">
    <svg class="shape" viewBox="0 0 665 345" preserveAspectRatio="none" aria-hidden="true">
      <defs>
        <linearGradient id="ea-band" x1="0" x2="1"><stop offset="0" stop-color="#2a4e9c"/><stop offset=".5" stop-color="#4d93d8"/><stop offset="1" stop-color="#2f4f9e"/></linearGradient>
      </defs>
      <path d="M0 0 H665 V0 Q300 40 0 100 Z" fill="#ffffff"/>
      <path d="M0 100 Q300 40 665 0 V24 Q300 64 0 120 Z" fill="url(#ea-band)"/>
      <path d="M0 120 Q300 64 665 24" fill="none" stroke="#fff" stroke-width="2"/>
    </svg>
    <div class="brand title"><span class="name">Curtis Hallorann</span><span class="sub">&amp; Associates</span></div>
    <span class="brand-dot"></span>
    <div class="brand side"><span class="name">Curtis Hallorann</span><span class="sub">&amp; Associates</span></div>
    <div class="window"></div>
    <div class="chips"><span class="chip">T 728 902 4471</span><span class="chip">F 728 902 4478</span><span class="chip">office@hallorann-eye.com</span></div>
    <p class="address">417 Pembrook Parkway Cedarbrook Falls, NY 11893</p>
  </section>

  <section class="piece card-front">
    <svg class="shape" viewBox="0 0 335 198" preserveAspectRatio="none" aria-hidden="true">
      <defs>
        <linearGradient id="cf-band" x1="0" x2="1"><stop offset="0" stop-color="#2a4e9c"/><stop offset=".5" stop-color="#4d93d8"/><stop offset="1" stop-color="#2f4f9e"/></linearGradient>
      </defs>
      <path d="M0 180 Q200 170 335 120 V198 H0 Z" fill="url(#cf-band)"/>
      <path d="M0 180 Q200 170 335 120" fill="none" stroke="#fff" stroke-width="2"/>
    </svg>
    <span class="brand-dot"></span>
    <div class="brand"><span class="name">Curtis Hallorann</span><span class="sub">&amp; Associates</span></div>
  </section>

  <section class="piece card-back">
    <span class="brand-dot"></span>
    <div class="brand"><span class="name">Curtis Hallorann</span><span class="sub">&amp; Associates</span></div>
    <span class="divider"></span>
    <div class="details">
      <p class="doctor">Marta Pelovska, O.D.</p>
      <p class="block">T &nbsp;728 902 4471<br>F &nbsp;728 902 4478<br>office@hallorann-eye.com</p>
      <p>417 Pembrook Parkway<br>Cedarbrook Falls,<br>NY 11893</p>
    </div>
  </section>

</body>
</html>
```